Business Card Design Project

I require a business card with the following information on them for various different people;
name
m:
f:
e:
I have a logo already and will attached that. We are in the construction industry. I require something clean and simple but eye catching at the same time. You can use another colour with our logo if you like and you can style the logo as well if you wish. I am open.
Also it needs to be front and back design.
Industry/Entity Type
Construction
Requirements
Must have
- Logo, name, mobile, fax and email address.
Front and back design

```html
<!DOCTYPE html>
<html lang="en">
<head>
<meta charset="utf-8">
<title>Stratabuild Business Card</title>
<link rel="stylesheet" href="https://fonts.googleapis.com/css2?family=Tinos:ital,wght@0,700;1,700&display=swap">
<style>
  :root {
    --card-white: #ffffff;
    --band-charcoal: #464646;
    --brand-green: #62b043;
    --label-white: #ffffff;
  }
  * { margin: 0; padding: 0; box-sizing: border-box; }
  html, body {
    width: 1200px;
    height: 721px;
    overflow: hidden;
    background: var(--card-white);
  }
  .card {
    position: relative;
    width: 1200px;
    height: 721px;
    background: var(--card-white);
    font-family: "Tinos", "Times New Roman", serif;
  }
  .brand {
    position: absolute;
    right: 67px;
    top: 182px;
    display: flex;
    align-items: center;
    gap: 18px;
  }
  .brand-square {
    width: 46px;
    height: 46px;
    background: var(--brand-green);
    border-radius: 4px;
  }
  .brand-name {
    font-weight: 700;
    font-style: normal;
    font-size: 58px;
    letter-spacing: 2px;
    color: var(--brand-green);
    line-height: 1;
  }
  .contact-band {
    position: absolute;
    left: 0;
    top: 425px;
    width: 1200px;
    height: 296px;
    background: var(--band-charcoal);
  }
  .contact-list {
    list-style: none;
    position: absolute;
    left: 29px;
    top: 8px;
  }
  .contact-label {
    font-weight: 700;
    font-style: italic;
    font-size: 43px;
    line-height: 64px;
    color: var(--label-white);
    white-space: nowrap;
  }
</style>
</head>
<body>
  <div class="card">
    <div class="brand">
      <span class="brand-square"></span>
      <span class="brand-name">STRATABUILD</span>
    </div>
    <div class="contact-band">
      <ul class="contact-list">
        <li class="contact-label">Name:</li>
        <li class="contact-label">Mobile:</li>
        <li class="contact-label">Fax:</li>
        <li class="contact-label">Email:</li>
      </ul>
    </div>
  </div>
</body>
</html>
```